Travel Group 'Lydgate Group' needs a new business card design

Lydgate Group is a diverse business specialising in bespoke, tailor made holidays to suit all budgets and we are specialists in planning exciting day/short trips to suit all markets. Our target market is very varied going from the corporate client and as well as people in the community who simply want to experience something special.
We are looking for a card design that will encourage people to look at our websites and social media platforms and to see for themselves the different facets to our business. It is essential that the card has social media icons for Friendly, Chirper and Picturo. We are looking for a card with a blank background with no pictures and for the front side to have the attached Lydgate logo. The card should have similar colour scheme to the attached Lydgate logo.
The card must have the following information on one side:
Maud Penrose
Business Development Manager
maudpenrose@lydgatevoyages.example
Lydgate Group, 87 Quarry Lane
Kilwinning, Ayrshire, Scotland KA19 4TN
+44 (0)1294 730182
And then the card must have the following on the second side:
(Lydgate logo)
(social media icons)
www.lydgatevoyages.example
www.lydgateoutings.example
Target Market(s)
Our target market is very varied going from the corporate client and as well as people in the community who simply want to experience something special.
Industry/Entity Type
Business
Contact Information for Business Card
Maud Penrose
+44 (0)1294 730182
(Lydgate logo)
(social media icons)
www.lydgatevoyages.example
www.lydgateoutings.example
Requirements
Must have
- It is essential that the card has social media icons for Friendly, Chirper & Picturo.
Should not have
- Should not have any images other than Lydgate logo.

```html
<!DOCTYPE html>
<html lang="en">
<head>
<meta charset="utf-8">
<title>Lydgate Group – Business Card</title>
<link rel="stylesheet" href="https://fonts.googleapis.com/css2?family=Sorts+Mill+Goudy&family=Cinzel:wght@500;700&display=swap">
<style>
  :root {
    --page: #ffffff;
    --ink: #272460;
    --plum: #4e1f5c;
    --band: #5e2463;
    --glow: #ecdfe8;
    --mauve: #94728a;
    --rose: #c172a6;
    --white: #ffffff;
  }
  * { margin: 0; padding: 0; box-sizing: border-box; }
  html, body {
    width: 1200px; height: 1200px; overflow: hidden;
    background: var(--page);
  }
  .sheet { position: relative; width: 1200px; height: 1200px; }
  .card {
    position: absolute; left: 186px; width: 840px; height: 481px;
    overflow: hidden;
    box-shadow: 6px 6px 8px rgba(0,0,0,0.35);
    font-family: "Sorts Mill Goudy", "Georgia", serif;
    color: var(--ink);
  }
  .card--front {
    top: 90px;
    background:
      radial-gradient(ellipse 48% 52% at 50% 45%, var(--glow) 35%, rgba(236,223,232,0) 100%),
      linear-gradient(135deg, var(--mauve) 0%, #a57d98 50%, var(--rose) 100%);
  }
  .card--back {
    top: 592px;
    background:
      radial-gradient(ellipse 55% 55% at 48% 45%, var(--glow) 40%, rgba(236,223,232,0) 100%),
      linear-gradient(135deg, #a2889c 0%, #b192ab 50%, var(--rose) 100%);
  }
  .wordmark {
    position: absolute; font-family: "Cinzel", "Georgia", serif;
    font-weight: 700; color: var(--ink); letter-spacing: 0.04em; white-space: nowrap;
  }
  .card--front .wordmark { left: 0; right: 0; top: 150px; text-align: center; font-size: 78px; }
  .card--back .wordmark { left: 62px; top: 118px; font-size: 46px; }
  .social {
    position: absolute; top: 340px; left: 0; right: 0;
    display: flex; justify-content: center; gap: 46px;
  }
  .social__item {
    display: flex; align-items: center; gap: 8px;
    font-size: 20px; color: var(--plum);
  }
  .social__mark { width: 26px; height: 26px; background: var(--plum); border-radius: 4px; }
  .websites {
    position: absolute; top: 410px; left: 0; right: 0;
    display: flex; justify-content: center; gap: 50px;
    font-size: 22px; letter-spacing: 0.02em; color: var(--ink);
  }
  .person { position: absolute; left: 424px; top: 52px; color: var(--plum); }
  .person__name {
    font-family: "Cinzel", "Georgia", serif; font-weight: 500;
    font-size: 50px; line-height: 1; letter-spacing: 0.02em; white-space: nowrap;
  }
  .person__role { font-size: 25px; margin-top: 6px; }
  .address {
    position: absolute; left: 59px; top: 259px;
    font-size: 26px; line-height: 28px; color: var(--plum);
  }
  .contact-band {
    position: absolute; left: 0; right: 0; bottom: 0; height: 66px;
    background: var(--band); color: var(--white);
    display: flex; align-items: center; justify-content: space-between;
    padding: 0 22px 0 29px; font-size: 21px; letter-spacing: 0.02em;
  }
  .contact { display: flex; align-items: center; gap: 10px; }
  .contact svg { width: 34px; height: 34px; }
</style>
</head>
<body>
<main class="sheet">
  <section class="card card--front" aria-label="Card front">
    <div class="wordmark">LYDGATE</div>
    <ul class="social" style="list-style:none">
      <li class="social__item"><span class="social__mark"></span>Friendly</li>
      <li class="social__item"><span class="social__mark"></span>Picturo</li>
      <li class="social__item"><span class="social__mark"></span>Chirper</li>
    </ul>
    <div class="websites">
      <span>www.lydgatevoyages.example</span>
      <span>www.lydgateoutings.example</span>
    </div>
  </section>

  <section class="card card--back" aria-label="Card back">
    <div class="wordmark">LYDGATE</div>
    <div class="person">
      <h1 class="person__name">MAUD PENROSE</h1>
      <p class="person__role">Business Development Manager</p>
    </div>
    <address class="address" style="font-style:normal">
      Lydgate Group, 87 Quarry Lane<br>
      Kilwinning, Ayrshire, Scotland KA19 4TN
    </address>
    <div class="contact-band">
      <div class="contact">
        <svg viewBox="0 0 34 34" aria-hidden="true">
          <circle cx="17" cy="17" r="15" fill="none" stroke="#fff" stroke-width="2"/>
          <rect x="9" y="11.5" width="16" height="11" rx="1.5" fill="none" stroke="#fff" stroke-width="1.8"/>
          <polyline points="9.5,12.5 17,18 24.5,12.5" fill="none" stroke="#fff" stroke-width="1.8"/>
        </svg>
        <span>maudpenrose@lydgatevoyages.example</span>
      </div>
      <div class="contact">
        <svg viewBox="0 0 34 34" aria-hidden="true">
          <circle cx="17" cy="17" r="15" fill="none" stroke="#fff" stroke-width="2"/>
          <path d="M12 9.5 l3 0 l1.5 4 l-2 1.5 c1 2.2 2.3 3.5 4.5 4.5 l1.5 -2 l4 1.5 l0 3 c0 1 -1 1.8 -2 1.8 c-6.5 -0.5 -11.8 -5.8 -12.3 -12.3 c0 -1 0.8 -2 1.8 -2 z" fill="#fff"/>
        </svg>
        <span>+44 (0)1294 730182</span>
      </div>
    </div>
  </section>
</main>
</body>
</html>
```